Vemtox homepage

Re-design www.vemtox.com. Visitors are developers and CTOs. Something simple and straightforward. Need different and special landingpage.
I like this page: http://flintmeadow.io/ (service is also similar).
Logo is at http://www.vemtox.com/vemtox.svg
Be bold with content you see on www.vemtox.com.
If you want ... make main message shorter, add links that doesn't exist, remove something etc.
Landing page should be cleaner than it is now.
Things what I want to have on page (missing on vemtox.com):
- testimonials
- contact form (can be simple as "send us e-mail...")
Vemtox supports KeldDb, Brimstackdb, Quorel and VX Rdb. You are welcome to use logos for those databases.
Target Market(s)
CTO-s and developers/programmers
Industry/Entity Type
It Service

```html
<!DOCTYPE html>
<html lang="en">
<head>
<meta charset="utf-8">
<title>Vemtox — Home</title>
<link rel="stylesheet" href="https://fonts.googleapis.com/css2?family=Tenor+Sans&family=Exo+2:ital,wght@1,500&family=Open+Sans:wght@400;700;800&family=Alegreya+Sans:ital,wght@1,400&display=swap">
<style>
  :root {
    --teal: #1dbdd0;
    --frame: #ddd8cc;
    --gold: #e6b52e;
    --ink: #2f2f36;
    --field: #edf1f1;
    --cyan-text: #19c6dc;
    --sage: #8fa88a;
    --sage-dark: #7c9774;
    --white: #ffffff;
  }
  * { box-sizing: border-box; margin: 0; padding: 0; }
  html, body { width: 1152px; height: 1200px; overflow: hidden; background: var(--white); }
  body { position: relative; font-family: "Open Sans", sans-serif; color: var(--ink); }

  .site-header {
    position: absolute; left: 0; top: 0; width: 1152px; height: 140px;
    background: var(--teal); border: 5px solid var(--frame); border-top-width: 4px;
  }
  .brand {
    position: absolute; left: 26px; top: 38px; display: flex; align-items: center; gap: 16px;
    font-family: "Open Sans", sans-serif; font-size: 58px; color: #4a4d55; line-height: 1;
  }
  .brand-mark { width: 44px; height: 44px; background: #3aa7d8; }
  .main-nav a, .sign-in {
    font-family: "Open Sans", sans-serif; font-variant: small-caps; font-weight: 800;
    font-size: 27px; color: var(--ink); text-decoration: none; line-height: 1;
    letter-spacing: 0.5px;
  }
  .main-nav a { position: absolute; top: 52px; }
  .nav-home { left: 436px; }
  .nav-download { left: 556px; }
  .nav-docs { left: 742px; }
  .sign-in {
    position: absolute; right: 0; top: 1px; width: 158px; height: 84px;
    background: var(--gold); display: flex; align-items: center; justify-content: center;
    color: #2a2a2a; font-size: 29px;
  }

  .hero-title {
    position: absolute; left: 176px; top: 162px; width: 880px; text-align: center;
    font-family: "Tenor Sans", sans-serif; font-variant: small-caps; font-size: 40px;
    line-height: 52px; color: #1e1e22; letter-spacing: 1px; transform: rotate(0.7deg);
    font-weight: 400;
  }
  .signup-lead {
    position: absolute; left: 10px; top: 286px; font-family: "Exo 2", sans-serif;
    font-style: italic; font-weight: 500; font-size: 25px; color: var(--cyan-text);
  }
  .signup-form .field {
    position: absolute; width: 303px; height: 52px; background: var(--field);
    padding-left: 22px; display: flex; align-items: center; font-size: 24px; color: #222;
  }
  .signup-form .start {
    position: absolute; left: 76px; top: 486px; width: 513px; height: 54px;
    background: var(--gold); display: flex; align-items: center; justify-content: center;
    font-size: 24px; color: #1f1f1f;
  }
  .hero-visual {
    position: absolute; left: 652px; top: 344px; width: 454px; height: 228px;
    background: linear-gradient(90deg, #d4d6da 0%, #eef3f6 35%, #7ab3e6 60%, #d94b45 78%, #4bb646 90%, #eef0f2 100%);
    border-radius: 6px; opacity: 0.85;
  }

  .section-band {
    position: absolute; left: 0; top: 591px; width: 1152px; height: 78px;
    background: var(--teal); border: 5px solid var(--frame); border-right: 0;
  }
  .section-band h2 {
    position: absolute; left: 318px; top: 50%; transform: translateY(-50%);
    font-family: "Open Sans", sans-serif; font-weight: 800; font-size: 46px;
    color: #35363d; line-height: 1; letter-spacing: 0.5px;
  }

  .feature {
    position: absolute; left: 0; top: 689px; width: 1152px; height: 511px; text-align: center;
  }
  .feature-bg {
    position: absolute; inset: 0;
    background: radial-gradient(ellipse at 55% 30%, #a9bd9f 0%, var(--sage) 55%, var(--sage-dark) 100%);
    border-top: 1px solid #555;
  }
  .feature-title {
    position: absolute; left: 0; right: 0; top: 82px; font-weight: 400;
    font-family: "Tenor Sans", sans-serif; font-variant: small-caps; font-size: 58px;
    color: var(--cyan-text); line-height: 1;
  }
  .feature-title span { border-bottom: 1px solid var(--cyan-text); padding-bottom: 4px; }
  .feature-text {
    position: absolute; left: 100px; top: 190px; width: 980px;
    font-family: "Alegreya Sans", sans-serif; font-style: italic; font-size: 56px;
    line-height: 65px; color: #1d1d1d; white-space: nowrap;
  }
  .read-more {
    position: absolute; right: 8px; top: 382px; font-family: "Alegreya Sans", sans-serif;
    font-style: italic; font-size: 34px; color: #1d1d1d; text-decoration: none;
    border-bottom: 1px solid #333;
  }
</style>
</head>
<body>
  <header class="site-header">
    <div class="brand"><span class="brand-mark"></span>vemtox</div>
    <nav class="main-nav">
      <a class="nav-home" href="#">Home</a>
      <a class="nav-download" href="#">Download</a>
      <a class="nav-docs" href="#">Documentation</a>
    </nav>
    <a class="sign-in" href="#">Sign In</a>
  </header>

  <h1 class="hero-title">Vemtox's unique architecture building<br>Enterprises, PaaS, Developer APIs,<br>Software</h1>

  <p class="signup-lead">Create Your Free Account Now!</p>
  <form class="signup-form">
    <div class="field" style="left:14px;top:346px">First Name</div>
    <div class="field" style="left:334px;top:346px">Last Name</div>
    <div class="field" style="left:17px;top:416px">Email Adress</div>
    <div class="field" style="left:336px;top:416px">Choose Password</div>
    <div class="start">Lets Gets Started!</div>
  </form>
  <div class="hero-visual" role="img" aria-label="Illustration of a database stack exchanging data with coloured cubes and documents"></div>

  <div class="section-band"><h2>Understand Vemtox</h2></div>

  <section class="feature">
    <div class="feature-bg" role="img" aria-label="Faded photo of analytics charts and reports on a desk"></div>
    <h2 class="feature-title"><span>Architecture</span></h2>
    <p class="feature-text">A high-level overview of the processes<br>using Vemtox with links to relevant<br>sections in documentation.</p>
    <a class="read-more" href="#">Read More</a>
  </section>
</body>
</html>
```